Secretary Business Cards for Golf Club

Hi I need a new business card designed.

I am the secretary at the Carrowen Golf Club - I take care of all the club functions & run the club on a day to day basis.

I don't want golf as the main feature I would like Functions to be the main focus.

Clean Crisp & Professional

Please include the following:

Carrowen Golf Club
Marguerite Vallance Secretary

"Thornby Park"
Bellmoor Ridge Road
WIRRALONG NSW 2795

Ph 02 - 6378 2405
Mobile 0471 326 815

carrowengolfclub@mailnestor.com

www.carrowengolfclub.com.au

```html
<!DOCTYPE html>
<html lang="en">
<head>
<meta charset="utf-8">
<title>Carrowen Golf Club – Secretary Business Cards</title>
<link rel="stylesheet" href="https://fonts.googleapis.com/css2?family=Arimo:wght@400;700&display=swap">
<style>
  :root {
    --backdrop: #e3e3e3;
    --club-green: #197a40;
    --deep-green: #1d6a35;
    --leaf-green: #5ea82c;
    --stripe-green: #3a9a5c;
    --border-green: #4f9a2c;
    --paper: #ffffff;
    --ink-white: #ffffff;
  }
  * { box-sizing: border-box; margin: 0; padding: 0; }
  html, body { width: 1200px; height: 960px; overflow: hidden; }
  body {
    background: var(--backdrop);
    font-family: "Arimo", Arial, sans-serif;
    position: relative;
  }

  .card {
    position: absolute;
    border-radius: 22px;
    overflow: hidden;
    box-shadow: 4px 6px 10px rgba(0,0,0,0.35);
  }

  /* Front card */
  .card-front {
    left: 62px; top: 44px; width: 788px; height: 449px;
    background: var(--club-green);
  }
  .front-mark {
    position: absolute; left: 50%; top: 176px;
    width: 64px; height: 64px; margin-left: -32px;
    border-radius: 50%;
    background: var(--leaf-green);
  }
  .front-name {
    position: absolute; left: 0; right: 0; top: 280px;
    display: flex; justify-content: center; align-items: center; gap: 18px;
  }
  .front-name .rule {
    width: 4px; height: 32px;
    border-left: 1px solid rgba(255,255,255,0.8);
    border-right: 1px solid rgba(255,255,255,0.8);
  }
  .front-name .club-name {
    color: var(--ink-white);
    font-size: 26px;
    font-variant: small-caps;
    letter-spacing: 1px;
  }
  .front-stripes {
    position: absolute; left: 0; right: 0; top: 368px;
  }
  .front-stripes span {
    display: block; height: 2px; background: var(--ink-white); margin-bottom: 6px;
  }

  /* Back card */
  .card-back {
    left: 358px; top: 460px; width: 758px; height: 434px;
    background: var(--paper);
  }
  .name-tag {
    position: absolute; left: 0; top: 16px; width: 188px; height: 24px;
    background: var(--leaf-green);
    color: var(--ink-white);
    font-size: 16px; font-variant: small-caps; letter-spacing: 0.5px;
    display: flex; align-items: center; justify-content: center;
  }
  .role {
    position: absolute; left: 108px; top: 40px;
    color: var(--deep-green); font-size: 14px;
  }
  .club-block {
    position: absolute; left: 89px; width: 300px; top: 122px;
    text-align: center; color: var(--deep-green);
  }
  .club-block .mark {
    width: 60px; height: 60px; border-radius: 50%;
    background: var(--club-green); margin: 0 auto 16px;
  }
  .club-block .club-name {
    font-size: 24px; font-variant: small-caps; letter-spacing: 0.5px;
    margin-bottom: 4px;
  }
  .club-block .address { font-size: 15px; line-height: 18px; }

  .contact-box {
    position: absolute; left: 425px; right: -4px; top: 146px; height: 136px;
    border: 1.5px solid var(--border-green);
    border-radius: 8px;
    padding: 8px 0 0 16px;
  }
  .contact-row {
    display: flex; align-items: center; gap: 10px;
    height: 29.5px;
    color: var(--deep-green); font-size: 14.5px;
  }
  .contact-row svg { flex: none; }

  .back-stripes {
    position: absolute; left: 0; right: 0; top: 349px;
  }
  .back-stripes span {
    display: block; height: 2px; background: var(--stripe-green); margin-bottom: 5px;
  }
</style>
</head>
<body>

<section class="card card-front" aria-label="Card front">
  <div class="front-mark"></div>
  <div class="front-name">
    <span class="rule"></span>
    <span class="club-name">Carrowen Golf Club</span>
    <span class="rule"></span>
  </div>
  <div class="front-stripes"><span></span><span></span><span></span></div>
</section>

<section class="card card-back" aria-label="Card back">
  <div class="name-tag">Marguerite Vallance</div>
  <div class="role">Secretary</div>

  <div class="club-block">
    <div class="mark"></div>
    <div class="club-name">Carrowen Golf Club</div>
    <div class="address">"Thornby Park"<br>Bellmoor Ridge Road<br>WIRRALONG NSW 2795</div>
  </div>

  <div class="contact-box">
    <div class="contact-row">
      <svg width="26" height="26" viewBox="0 0 26 26"><circle cx="13" cy="13" r="13" fill="var(--deep-green)"/><rect x="9" y="6" width="8" height="14" rx="1.5" fill="none" stroke="#fff" stroke-width="1.5"/><line x1="11.5" y1="17.5" x2="14.5" y2="17.5" stroke="#fff" stroke-width="1.2"/></svg>
      <span>0471 326 815</span>
    </div>
    <div class="contact-row">
      <svg width="26" height="26" viewBox="0 0 26 26"><circle cx="13" cy="13" r="13" fill="var(--deep-green)"/><path d="M6 11 q7 -5 14 0 v2 h-3 v-2 h-8 v2 h-3z" fill="#fff"/><rect x="8" y="13" width="10" height="6" rx="1" fill="#fff"/></svg>
      <span>02 - 6378 2405</span>
    </div>
    <div class="contact-row">
      <svg width="26" height="26" viewBox="0 0 26 26"><circle cx="13" cy="13" r="13" fill="var(--deep-green)"/><rect x="6.5" y="8.5" width="13" height="9" fill="none" stroke="#fff" stroke-width="1.4"/><path d="M6.5 8.5 l6.5 5 l6.5 -5" fill="none" stroke="#fff" stroke-width="1.4"/></svg>
      <span>carrowengolfclub@mailnestor.com</span>
    </div>
    <div class="contact-row">
      <svg width="26" height="26" viewBox="0 0 26 26"><circle cx="13" cy="13" r="13" fill="var(--deep-green)"/><g fill="none" stroke="#fff" stroke-width="1.2"><circle cx="13" cy="13" r="7"/><ellipse cx="13" cy="13" rx="3" ry="7"/><line x1="6" y1="13" x2="20" y2="13"/></g></svg>
      <span>www.carrowengolfclub.com.au</span>
    </div>
  </div>

  <div class="back-stripes"><span></span><span></span><span></span><span></span></div>
</section>

</body>
</html>
```